Webdesign für Online-Shop für Honig
Zielgruppe
Verkauf von Sidr Honig. Ein sehr hochwertiger Premium-Honig aus dem Jemen.
Aufgabenstellung
Zu Erstellen ist ein Design für einen Onlineshop. Der Onlineshop verkauft Kosmetik-, Lebensmittel- und Gesundheitsprodukte die alle auf einem Honig basieren.
Domain: qalvenu.com
Die Seite soll sehr hochwertig und orientalisch wirken. Der Hintergrund soll auf jeden Fall dunkel sein.
Wir benötigen ein Screendesign der:
- Home-Seite,
- Über uns-Seite
- Produktdetailseite.
Die Designs müssen nicht per HTML umgesetzt werden, können aber. Es reicht ein reines Design als Bild, HTML ist aber auch in Ordnung.
Bitte hochwertige Stockbilder nutzen.

```html
<!DOCTYPE html>
<html lang="de">
<head>
<meta charset="utf-8">
<title>Qalvenu – About us</title>
<link href="https://fonts.googleapis.com/css2?family=Cormorant+Garamond:wght@300;400&family=Crimson+Text:wght@400&family=Mrs+Saint+Delafield&display=swap" rel="stylesheet">
<style>
  :root {
    --bg: #000000;
    --gold: #c98e58;
    --gold-soft: #d6a06c;
    --ornament: #3b2a18;
    --ornament-fade: rgba(59, 42, 24, 0);
    --honey-light: #f7e7a0;
    --honey: #e8b93a;
    --steel: #9aa3a3;
  }
  * { margin: 0; padding: 0; box-sizing: border-box; }
  html, body { width: 1200px; height: 2480px; overflow: hidden; background: var(--bg); }
  .page {
    position: relative; width: 1200px; height: 2480px; overflow: hidden;
    background: var(--bg); color: var(--gold);
    font-family: "Crimson Text", Georgia, serif;
  }
  .ornament { position: absolute; border-radius: 50%; }
  .ornament--left { left: -170px; top: 40px; width: 540px; height: 760px;
    background: radial-gradient(closest-side, var(--ornament), var(--ornament-fade)); opacity: .75; }
  .ornament--right { left: 860px; top: 90px; width: 560px; height: 700px;
    background: radial-gradient(closest-side, var(--ornament), var(--ornament-fade)); opacity: .75; }
  .ornament--footer { left: 250px; top: 2110px; width: 700px; height: 560px;
    background: radial-gradient(closest-side, var(--ornament), var(--ornament-fade)); opacity: .7; }

  .brand { position: absolute; font-family: "Cormorant Garamond", Georgia, serif; font-weight: 400;
    color: var(--gold); letter-spacing: 2px; text-transform: uppercase; }
  .brand--header { left: 96px; top: 82px; font-size: 20px; }
  .tagline { position: absolute; left: 198px; top: 70px; font-family: "Mrs Saint Delafield", cursive;
    font-size: 34px; color: var(--gold); }

  .icon-bag { position: absolute; left: 974px; top: 80px; }
  .icon-menu { position: absolute; left: 1034px; top: 84px; }

  .page-title { position: absolute; left: 0; top: 228px; font-family: "Cormorant Garamond", Georgia, serif;
    font-weight: 300; font-size: 126px; line-height: 108px; color: var(--gold); letter-spacing: -1px; }

  .title-mark { position: absolute; left: 130px; top: 476px; width: 18px; height: 18px; border-radius: 50%;
    background: radial-gradient(var(--gold), rgba(201,142,88,.2)); }

  .intro { position: absolute; left: 126px; top: 506px; width: 372px; font-size: 15.5px; line-height: 22.4px;
    color: var(--gold-soft); }

  .script { position: absolute; font-family: "Mrs Saint Delafield", cursive; color: var(--gold); white-space: nowrap; }
  .script--manufacture { left: 740px; top: 690px; font-size: 76px; }
  .script--bee { left: 290px; top: 1860px; font-size: 76px; }

  .frame { position: absolute; border: 1px solid var(--gold); }
  .frame--manufacture { left: 587px; top: 774px; width: 334px; height: 420px; }
  .frame--bee { left: 151px; top: 1454px; width: 333px; height: 432px; }

  .photo { position: absolute; }
  .photo--manufacture { left: 566px; top: 781px; width: 335px; height: 437px;
    background: linear-gradient(100deg, #c9cfc6 0%, var(--steel) 35%, #b8a24a 60%, #d8c56a 75%, #8c8e7e 100%); }
  .photo--bee { left: 133px; top: 1470px; width: 335px; height: 420px;
    background: radial-gradient(circle at 45% 60%, #b88a1c 0%, var(--honey) 35%, var(--honey-light) 100%); }

  .caption { position: absolute; font-size: 15.5px; line-height: 22.4px; color: var(--gold-soft); width: 130px; }
  .caption--manufacture { left: 941px; top: 1104px; }
  .caption--bee { left: 501px; top: 1789px; }

  .quote { position: absolute; left: 548px; top: 1280px; font-family: "Mrs Saint Delafield", cursive;
    font-size: 84px; line-height: 75px; color: var(--gold); white-space: nowrap; }
  .quote__mark { display: block; margin-left: 28px; font-size: 70px; line-height: 50px; }
  .quote__line--indent { margin-left: 24px; }

  .footer-rule { position: absolute; left: 130px; top: 2236px; width: 936px; border-top: 2px dotted var(--gold); }
  .brand--footer { left: 130px; top: 2296px; font-size: 18px; }
  .footer-col { position: absolute; top: 2298px; font-size: 15.5px; line-height: 22px; color: var(--gold-soft); }
  .footer-col--address { left: 239px; }
  .footer-col--categories { left: 526px; }
  .footer-col--legal { left: 744px; }
  .to-top { position: absolute; left: 1128px; top: 2354px; }
</style>
</head>
<body>
<div class="page">
  <div class="ornament ornament--left" role="img" aria-label="Faint oriental mandala ornament"></div>
  <div class="ornament ornament--right" role="img" aria-label="Faint oriental mandala ornament"></div>
  <div class="ornament ornament--footer" role="img" aria-label="Faint oriental mandala ornament"></div>

  <header>
    <div class="brand brand--header">Qalvenu</div>
    <div class="tagline">more than just a honey</div>
    <svg class="icon-bag" width="22" height="28" viewBox="0 0 22 28" fill="none" stroke="var(--gold)" stroke-width="2">
      <rect x="2" y="8" width="18" height="18"/>
      <path d="M7 8 V5 a4 4 0 0 1 8 0 V8"/>
    </svg>
    <svg class="icon-menu" width="64" height="22" viewBox="0 0 64 22" stroke="var(--gold)" stroke-width="2">
      <line x1="0" y1="2" x2="56" y2="2"/>
      <line x1="8" y1="10" x2="64" y2="10"/>
      <line x1="0" y1="18" x2="56" y2="18"/>
    </svg>
  </header>

  <h1 class="page-title">ABOUT<br>US</h1>
  <div class="title-mark" role="img" aria-label="Small floral ornament"></div>

  <p class="intro">Lorem ipsum dolor sit amet, conLorem ipsum dolor sit amet, consectetuer adipiscing elit, sed diam nonummy nibh euismod tincidunt ut laoreet dolore magna aliquam erat volutpat. Ut wisi enim ad minim veniam, quis nostrud exerci tation ullamcorper suscipit lobortis nisl ut aliquip ex ea commodo consequat. Duis autem vel Lorem ipsum dolor sit amet, consectetuer adipiscing elit, sed diam nonummy nibh euismod tincidunt ut laoreet dolore magna aliquam erat volutpat. Ut wisi enim ad minim veniam, quis nostrud exerci tation ullamcorper suscipit lobortis nisl ut aliquip ex ea commodo consequat. Duis autem vel eum iriure dolor in hendrerit in vulputate velit esse molestie consequat, vel illum dolore eu feugiat nulla facilisis at vero eros et accumsan et iusto odio dignissim qui blandit praesent luptatum zzril delenit augue duis dolore te feugait nulla facilisi. Lorem ipsum dolor sit amet.</p>

  <section class="feature feature--manufacture">
    <div class="frame frame--manufacture"></div>
    <div class="photo photo--manufacture" role="img" aria-label="Honey flowing from steel filling nozzles on a production line"></div>
    <div class="script script--manufacture">manufacture</div>
    <p class="caption caption--manufacture">Ut wisi enim ad minim veniam, tion ullamcorper suscipit lob.</p>
  </section>

  <blockquote class="quote">
    <span class="quote__mark">"</span>
    <span class="quote__line">This is a short</span><br>
    <span class="quote__line quote__line--indent">statement to how we</span><br>
    <span class="quote__line quote__line--indent">create aur products"</span>
  </blockquote>

  <section class="feature feature--bee">
    <div class="frame frame--bee"></div>
    <div class="photo photo--bee" role="img" aria-label="Close-up of a bee on golden honeycomb"></div>
    <div class="script script--bee">busy bee</div>
    <p class="caption caption--bee">Ut wisi enim ad minim veniam, tion ullamcorper suscipit lob.</p>
  </section>

  <footer>
    <div class="footer-rule"></div>
    <div class="brand brand--footer">Qalvenu</div>
    <div class="footer-col footer-col--address">QALVENU PREMIUM HONEY<br>Street Number 123<br>1234 City</div>
    <div class="footer-col footer-col--categories">Healthy<br>Beauty<br>Tasty</div>
    <div class="footer-col footer-col--legal">Impressum<br>AGB</div>
    <svg class="to-top" width="58" height="58" viewBox="0 0 58 58" fill="none" stroke="var(--gold)" stroke-width="1.5">
      <circle cx="29" cy="29" r="28"/>
      <path d="M14 35 L29 20 L44 35"/>
    </svg>
  </footer>
</div>
</body>
</html>
```